Ridge Fitness & Training Design

See photo attached
Obviously I want that second logo attached to it.
Ridge Fitness & Training instead of the old one.
I had business cards already but I want to go back to a more professional look.
Open the some ideas but I would love around the same look that is shown on the photos. Easy money I would say for a designer

Target Market(s)

Fitness

Industry/Entity Type

Business

Contact Information for Business Card

Maxime Delorne
Director, Strength & Conditioning Head Coach
148 Carrow Street - Melbourne, Australia VIC 3000
0461092436
ABN 83104629578
mdelorne@ridgefitnessandtraining.com
www.ridgefitnessandtraining.com
facebook.com/ridgefitnessandtraining.com

Requirements
Must have
• Look Professional same or similar to uploaded photos.
• open to creativity
• black colour

```html
<!DOCTYPE html>
<html lang="en">
<head>
<meta charset="utf-8">
<title>Ridge Fitness &amp; Training – Business Cards</title>
<link rel="stylesheet" href="https://fonts.googleapis.com/css2?family=PT+Sans+Narrow:wght@400;700&display=swap">
<style>
  :root {
    --backdrop: #2b2b2d;
    --card: #231f20;
    --red: #c8202d;
    --white: #ffffff;
    --muted: #d9d9d9;
  }
  * { margin: 0; padding: 0; box-sizing: border-box; }
  html, body { width: 1200px; height: 900px; overflow: hidden; }
  body {
    background: var(--backdrop);
    font-family: "PT Sans Narrow", "Arial Narrow", sans-serif;
    color: var(--white);
    position: relative;
  }
  .card {
    position: absolute;
    width: 513px;
    height: 296px;
    background: var(--card);
    box-shadow: 0 2px 6px rgba(0,0,0,.45);
  }
  .card--1 { left: 72px;  top: 138px; }
  .card--2 { left: 615px; top: 138px; }
  .card--3 { left: 72px;  top: 464px; }
  .card--4 { left: 615px; top: 464px; }

  .brand-mark {
    position: absolute;
    left: 22px; top: 112px;
    width: 210px;
    text-align: center;
    font-weight: 700;
    font-size: 27px;
    line-height: 1.05;
    letter-spacing: 1px;
    color: var(--white);
    text-transform: uppercase;
  }
  .divider {
    position: absolute;
    left: 248px; top: 28px;
    width: 2px; height: 248px;
    background: var(--white);
  }
  .details {
    position: absolute;
    left: 266px; top: 33px;
    width: 240px;
  }
  .wordmark {
    font-weight: 700;
    font-size: 21px;
    letter-spacing: 1.2px;
    line-height: 1;
    color: var(--white);
    text-transform: uppercase;
    white-space: nowrap;
  }
  .person { margin-top: 22px; height: 64px; }
  .person__name {
    font-weight: 700;
    font-size: 14px;
    color: var(--red);
    text-transform: uppercase;
    line-height: 1.1;
  }
  .person__role {
    font-weight: 700;
    font-size: 10.5px;
    line-height: 1.3;
    color: var(--muted);
  }
  .person__abn {
    font-size: 7.5px;
    line-height: 1.2;
    color: var(--muted);
  }
  .contact { list-style: none; }
  .contact li {
    display: flex;
    align-items: center;
    font-weight: 700;
    font-size: 10.5px;
    line-height: 13.5px;
    color: var(--muted);
    white-space: nowrap;
  }
  .contact .icon {
    width: 13px;
    flex: none;
    margin-right: 6px;
    display: flex;
    justify-content: center;
  }
  .contact .icon svg { display: block; }
  .contact--phone { margin-top: 0; }
  .contact--place { margin-top: 13px; }
  .contact--online { margin-top: 15px; }
  .contact--place li { align-items: flex-start; }
  .contact .indent { padding-left: 19px; }
  .square-mark { width: 9px; height: 9px; background: var(--red); }
</style>
</head>
<body>

<!-- Card: Maxime Delorne -->
<article class="card card--1">
  <div class="brand-mark">Ridge Fitness<br>&amp; Training</div>
  <div class="divider"></div>
  <div class="details">
    <div class="wordmark">Ridge Fitness &amp; Training</div>
    <div class="person">
      <div class="person__name">Maxime Delorne</div>
      <div class="person__role">Director<br>Strength &amp; Conditioning Head Coach</div>
      <div class="person__abn">ABN 83104629578</div>
    </div>
    <ul class="contact contact--phone">
      <li><span class="icon"><svg width="10" height="10" viewBox="0 0 10 10"><circle cx="5" cy="5" r="4.3" fill="none" stroke="#c8202d" stroke-width="1"/><path d="M3.4 2.6 Q2.6 5.4 5.6 7.2" fill="none" stroke="#c8202d" stroke-width="1.3"/></svg></span>0461 092 436</li>
    </ul>
    <ul class="contact contact--place">
      <li><span class="icon"><svg width="9" height="12" viewBox="0 0 9 12"><path d="M4.5 0.5a4 4 0 0 1 4 4c0 3-4 7-4 7s-4-4-4-7a4 4 0 0 1 4-4z" fill="#c8202d"/><circle cx="4.5" cy="4.5" r="1.5" fill="#231f20"/></svg></span>Level 2 &amp; 3, 148 Carrow Street</li>
      <li class="indent">Melbourne, VIC 3000 Australia</li>
    </ul>
    <ul class="contact contact--online">
      <li><span class="icon"><svg width="11" height="8" viewBox="0 0 11 8"><rect width="11" height="8" fill="#c8202d"/><path d="M0 0 L5.5 4.5 L11 0" fill="none" stroke="#231f20" stroke-width="1"/></svg></span>mdelorne@ridgefitnessandtraining.com</li>
      <li><span class="icon"><span class="square-mark"></span></span>/ridgefitnessandtraining.com</li>
      <li><span class="icon"><svg width="10" height="10" viewBox="0 0 10 10"><circle cx="5" cy="5" r="4.3" fill="none" stroke="#c8202d" stroke-width="1"/><ellipse cx="5" cy="5" rx="2" ry="4.3" fill="none" stroke="#c8202d" stroke-width="0.8"/><line x1="0.7" y1="5" x2="9.3" y2="5" stroke="#c8202d" stroke-width="0.8"/></svg></span>www.ridgefitnessandtraining.com</li>
    </ul>
  </div>
</article>

<!-- Card: Tomas Ferrand -->
<article class="card card--2">
  <div class="brand-mark">Ridge Fitness<br>&amp; Training</div>
  <div class="divider"></div>
  <div class="details">
    <div class="wordmark">Ridge Fitness &amp; Training</div>
    <div class="person">
      <div class="person__name">Tomas Ferrand</div>
      <div class="person__role">Operations Manager<br>Strength &amp; Conditioning Coach</div>
      <div class="person__abn">ABN 83104629578</div>
    </div>
    <ul class="contact contact--phone">
      <li><span class="icon"><svg width="10" height="10" viewBox="0 0 10 10"><circle cx="5" cy="5" r="4.3" fill="none" stroke="#c8202d" stroke-width="1"/><path d="M3.4 2.6 Q2.6 5.4 5.6 7.2" fill="none" stroke="#c8202d" stroke-width="1.3"/></svg></span>0452 318 704</li>
    </ul>
    <ul class="contact contact--place">
      <li><span class="icon"><svg width="9" height="12" viewBox="0 0 9 12"><path d="M4.5 0.5a4 4 0 0 1 4 4c0 3-4 7-4 7s-4-4-4-7a4 4 0 0 1 4-4z" fill="#c8202d"/><circle cx="4.5" cy="4.5" r="1.5" fill="#231f20"/></svg></span>Level 4, 83 Elmwood Street</li>
      <li class="indent">Melbourne, VIC 3000 Australia</li>
    </ul>
    <ul class="contact contact--online">
      <li><span class="icon"><svg width="11" height="8" viewBox="0 0 11 8"><rect width="11" height="8" fill="#c8202d"/><path d="M0 0 L5.5 4.5 L11 0" fill="none" stroke="#231f20" stroke-width="1"/></svg></span>tferrand@ridgefitnessandtraining.com</li>
      <li><span class="icon"><span class="square-mark"></span></span>/ridgefitnessandtraining.com</li>
      <li><span class="icon"><svg width="10" height="10" viewBox="0 0 10 10"><circle cx="5" cy="5" r="4.3" fill="none" stroke="#c8202d" stroke-width="1"/><ellipse cx="5" cy="5" rx="2" ry="4.3" fill="none" stroke="#c8202d" stroke-width="0.8"/><line x1="0.7" y1="5" x2="9.3" y2="5" stroke="#c8202d" stroke-width="0.8"/></svg></span>www.ridgefitnessandtraining.com</li>
    </ul>
  </div>
</article>

<!-- Card: Lucas Henmore -->
<article class="card card--3">
  <div class="brand-mark">Ridge Fitness<br>&amp; Training</div>
  <div class="divider"></div>
  <div class="details">
    <div class="wordmark">Ridge Fitness &amp; Training</div>
    <div class="person">
      <div class="person__name">Lucas Henmore</div>
      <div class="person__role">Marketing Manager<br>Strength &amp; Conditioning Coach Operations Manager</div>
      <div class="person__abn">ABN 83104629578</div>
    </div>
    <ul class="contact contact--phone">
      <li><span class="icon"><svg width="10" height="10" viewBox="0 0 10 10"><circle cx="5" cy="5" r="4.3" fill="none" stroke="#c8202d" stroke-width="1"/><path d="M3.4 2.6 Q2.6 5.4 5.6 7.2" fill="none" stroke="#c8202d" stroke-width="1.3"/></svg></span>0417 263 851</li>
    </ul>
    <ul class="contact contact--place">
      <li><span class="icon"><svg width="9" height="12" viewBox="0 0 9 12"><path d="M4.5 0.5a4 4 0 0 1 4 4c0 3-4 7-4 7s-4-4-4-7a4 4 0 0 1 4-4z" fill="#c8202d"/><circle cx="4.5" cy="4.5" r="1.5" fill="#231f20"/></svg></span>Level 4, 83 Elmwood Street</li>
      <li class="indent">Melbourne, VIC 3000 Australia</li>
    </ul>
    <ul class="contact contact--online">
      <li><span class="icon"><svg width="11" height="8" viewBox="0 0 11 8"><rect width="11" height="8" fill="#c8202d"/><path d="M0 0 L5.5 4.5 L11 0" fill="none" stroke="#231f20" stroke-width="1"/></svg></span>lhenmore@ridgefitnessandtraining.com</li>
      <li><span class="icon"><span class="square-mark"></span></span>/ridgefitnessandtraining.com</li>
      <li><span class="icon"><svg width="10" height="10" viewBox="0 0 10 10"><circle cx="5" cy="5" r="4.3" fill="none" stroke="#c8202d" stroke-width="1"/><ellipse cx="5" cy="5" rx="2" ry="4.3" fill="none" stroke="#c8202d" stroke-width="0.8"/><line x1="0.7" y1="5" x2="9.3" y2="5" stroke="#c8202d" stroke-width="0.8"/></svg></span>www.ridgefitnessandtraining.com</li>
    </ul>
  </div>
</article>

<!-- Card: Nina Vashti -->
<article class="card card--4">
  <div class="brand-mark">Ridge Fitness<br>&amp; Training</div>
  <div class="divider"></div>
  <div class="details">
    <div class="wordmark">Ridge Fitness &amp; Training</div>
    <div class="person">
      <div class="person__name">Nina Vashti</div>
      <div class="person__role">Strength &amp; Conditioning Coach</div>
      <div class="person__abn">ABN 83104629578</div>
    </div>
    <ul class="contact contact--phone">
      <li><span class="icon"><svg width="10" height="10" viewBox="0 0 10 10"><circle cx="5" cy="5" r="4.3" fill="none" stroke="#c8202d" stroke-width="1"/><path d="M3.4 2.6 Q2.6 5.4 5.6 7.2" fill="none" stroke="#c8202d" stroke-width="1.3"/></svg></span>0414 906 237</li>
    </ul>
    <ul class="contact contact--place">
      <li><span class="icon"><svg width="9" height="12" viewBox="0 0 9 12"><path d="M4.5 0.5a4 4 0 0 1 4 4c0 3-4 7-4 7s-4-4-4-7a4 4 0 0 1 4-4z" fill="#c8202d"/><circle cx="4.5" cy="4.5" r="1.5" fill="#231f20"/></svg></span>Level 4, 83 Elmwood Street</li>
      <li class="indent">Melbourne, VIC 3000 Australia</li>
    </ul>
    <ul class="contact contact--online">
      <li><span class="icon"><svg width="11" height="8" viewBox="0 0 11 8"><rect width="11" height="8" fill="#c8202d"/><path d="M0 0 L5.5 4.5 L11 0" fill="none" stroke="#231f20" stroke-width="1"/></svg></span>nvashti@ridgefitnessandtraining.com</li>
      <li><span class="icon"><span class="square-mark"></span></span>/ridgefitnessandtraining.com</li>
      <li><span class="icon"><svg width="10" height="10" viewBox="0 0 10 10"><circle cx="5" cy="5" r="4.3" fill="none" stroke="#c8202d" stroke-width="1"/><ellipse cx="5" cy="5" rx="2" ry="4.3" fill="none" stroke="#c8202d" stroke-width="0.8"/><line x1="0.7" y1="5" x2="9.3" y2="5" stroke="#c8202d" stroke-width="0.8"/></svg></span>www.ridgefitnessandtraining.com</li>
    </ul>
  </div>
</article>

</body>
</html>
```